Pipelining Product Supply Company Needs New Stationery

We need new stationery (letter head, with compliments slips & business card) for our industry leading pipe lining supply company. basically we sell product to other plumbers to carry out pipe relining.

Im looking for something, fresh, professional, sleek and modern at the same time.

Ive attached a copy of the logo and also some guidelines to follow for colours and fonts etc.

Target Market(s)

Plumbers

Industry/Entity Type

Plumbing

Font styles to use
Sans Serif

Requirements
Must have
• The logo, space for ABN, Address, Phone Number, website and email.
Nice to have
• Stand out from the crowd. To look sleep and professional.
Should not have
• Any other colours apart from what is on the guidelines.

```html
<!DOCTYPE html>
<html lang="en">
<head>
<meta charset="utf-8">
<title>Kestrel Relining – Stationery Set</title>
<link rel="stylesheet" href="https://fonts.googleapis.com/css2?family=Montserrat:wght@600;700&family=Questrial&display=swap">
<style>
  :root {
    --backdrop: #939598;
    --paper: #ffffff;
    --ink-dark: #0b0f14;
    --brand-green: #6cb33f;
    --brand-grey: #6d6e71;
    --text-light: #e9ecef;
    --font-display: "Montserrat", Arial, sans-serif;
    --font-body: "Questrial", "Century Gothic", sans-serif;
  }
  * { box-sizing: border-box; margin: 0; padding: 0; }
  html, body { width: 1200px; height: 845px; overflow: hidden; }
  body { background: var(--backdrop); position: relative; font-family: var(--font-body); }

  .sheet { position: absolute; background: var(--paper); overflow: hidden; box-shadow: 0 1px 3px rgba(0,0,0,.25); }
  .letterhead { left: 34px; top: 34px; width: 549px; height: 777px; }
  .comp-slip { left: 617px; top: 203px; width: 549px; height: 259px; }
  .card-front { left: 660px; top: 495px; width: 223px; height: 144px; }
  .card-back { left: 900px; top: 495px; width: 223px; height: 144px; background: var(--ink-dark); }

  /* brand lockup */
  .brand { position: absolute; display: flex; align-items: center; gap: 7px; color: var(--brand-green);
           font-family: var(--font-display); font-weight: 700; white-space: nowrap; letter-spacing: .02em; }
  .brand-square { background: var(--brand-green); flex: none; }
  .letterhead .brand { left: 0; right: 0; justify-content: center; top: 50px; font-size: 21px; }
  .letterhead .brand-square { width: 14px; height: 14px; }
  .comp-slip .brand { left: 0; right: 0; justify-content: center; top: 55px; font-size: 21px; }
  .comp-slip .brand-square { width: 14px; height: 14px; }
  .card-front .brand { right: 9px; top: 37px; font-size: 10.5px; gap: 4px; }
  .card-front .brand-square { width: 8px; height: 8px; }
  .card-back .brand { left: 0; right: 0; justify-content: center; top: 64px; font-size: 13px; gap: 5px; }
  .card-back .brand-square { width: 9px; height: 9px; }

  /* footer bands */
  .footer-band { position: absolute; left: 0; right: 0; bottom: 0; }
  .footer-band svg.band-shape { position: absolute; inset: 0; display: block; }
  .band-dark { fill: var(--ink-dark); }
  .band-green { fill: var(--brand-green); }
  .letterhead .footer-band, .comp-slip .footer-band { height: 60px; }
  .card-front .footer-band { height: 62px; }

  .footer-web { position: absolute; left: 41px; top: 33px; color: #fff; font-family: var(--font-display);
                font-weight: 700; font-size: 10.5px; letter-spacing: .01em; }
  .footer-col { position: absolute; top: 28px; color: var(--text-light); font-size: 8.2px; line-height: 12.5px; }
  .footer-col.col-legal { left: 222px; }
  .footer-col.col-contact { left: 390px; }
  .info-line { display: flex; align-items: center; gap: 4px; white-space: nowrap; }
  .info-line svg { width: 7px; height: 7px; fill: var(--brand-green); flex: none; }

  .compliments-label { position: absolute; right: 10px; top: 187px; color: var(--brand-green);
                       font-size: 15px; letter-spacing: .02em; }

  /* business card front */
  .holder { position: absolute; left: 9px; top: 33px; }
  .holder-name { font-family: var(--font-display); font-weight: 700; font-size: 8.6px; color: var(--ink-dark); letter-spacing: .01em; }
  .holder-role { font-size: 6.8px; color: var(--ink-dark); margin-top: 1px; }
  .card-contact { position: absolute; left: 9px; top: 29px; color: var(--text-light); font-size: 6px; line-height: 10.8px; }
  .card-contact .info-line svg { width: 5.5px; height: 5.5px; }
  .card-address { position: absolute; right: 9px; top: 30px; text-align: right; color: var(--text-light);
                  font-size: 6px; line-height: 10.2px; }
</style>
</head>
<body>

<svg width="0" height="0" style="position:absolute" aria-hidden="true">
  <symbol id="icon-tick" viewBox="0 0 10 10"><circle cx="5" cy="5" r="5"/><path d="M2.6 5.2l1.7 1.6 3.2-3.4" fill="none" stroke="#0b0f14" stroke-width="1.4"/></symbol>
  <symbol id="icon-pin" viewBox="0 0 10 10"><path d="M5 0a3.6 3.6 0 0 0-3.6 3.6C1.4 6.4 5 10 5 10s3.6-3.6 3.6-6.4A3.6 3.6 0 0 0 5 0zm0 5.1a1.5 1.5 0 1 1 0-3 1.5 1.5 0 0 1 0 3z"/></symbol>
  <symbol id="icon-phone" viewBox="0 0 10 10"><path d="M2.2 0.4l1.6 2.1-1 1.1c.6 1.3 1.5 2.2 2.8 2.8l1.1-1 2.1 1.6-.8 1.9C4.6 8.8 1.2 5.4.3 1.2z"/></symbol>
  <symbol id="icon-mail" viewBox="0 0 10 10"><path d="M0 2h10v6H0z"/><path d="M0 2l5 3.4L10 2" fill="none" stroke="#0b0f14" stroke-width="1"/></symbol>
  <symbol id="icon-globe" viewBox="0 0 10 10"><circle cx="5" cy="5" r="5"/><path d="M0 5h10M5 0c2 2.5 2 7.5 0 10M5 0c-2 2.5-2 7.5 0 10" fill="none" stroke="#0b0f14" stroke-width=".8"/></symbol>
</svg>

<!-- Letterhead -->
<section class="sheet letterhead" aria-label="Letterhead">
  <div class="brand"><span class="brand-square"></span>KESTREL RELINING</div>
  <footer class="footer-band">
    <svg class="band-shape" viewBox="0 0 549 60" preserveAspectRatio="none" aria-hidden="true">
      <path class="band-dark" d="M0 0H134Q140 0 143 6L147 13Q149 17 155 17H549V60H0Z"/>
      <rect class="band-green" x="150" y="11" width="399" height="5"/>
    </svg>
    <div class="footer-web">www.KestrelRelining.com.au</div>
    <div class="footer-col col-legal">
      <div class="info-line"><svg><use href="#icon-tick"/></svg>ABN: 12 345 678 901</div>
      <div class="info-line"><svg><use href="#icon-pin"/></svg>14 Harbour Lane Dunmore NSW 2529</div>
    </div>
    <div class="footer-col col-contact">
      <div class="info-line"><svg><use href="#icon-phone"/></svg>1-300-555-014</div>
      <div class="info-line"><svg><use href="#icon-mail"/></svg>hello@KestrelRelining.com.au</div>
    </div>
  </footer>
</section>

<!-- With compliments slip -->
<section class="sheet comp-slip" aria-label="With compliments slip">
  <div class="brand"><span class="brand-square"></span>KESTREL RELINING</div>
  <div class="compliments-label">WITH COMPLIMENTS</div>
  <footer class="footer-band">
    <svg class="band-shape" viewBox="0 0 549 60" preserveAspectRatio="none" aria-hidden="true">
      <path class="band-dark" d="M0 0H135Q141 0 144 6L148 13Q150 17 156 17H549V60H0Z"/>
      <rect class="band-green" x="151" y="11" width="398" height="5"/>
    </svg>
    <div class="footer-web">www.KestrelRelining.com.au</div>
    <div class="footer-col col-legal">
      <div class="info-line"><svg><use href="#icon-tick"/></svg>ABN: 12 345 678 901</div>
      <div class="info-line"><svg><use href="#icon-pin"/></svg>14 Harbour Lane Dunmore NSW 2529</div>
    </div>
    <div class="footer-col col-contact">
      <div class="info-line"><svg><use href="#icon-phone"/></svg>1-300-555-014</div>
      <div class="info-line"><svg><use href="#icon-mail"/></svg>hello@KestrelRelining.com.au</div>
    </div>
  </footer>
</section>

<!-- Business card front -->
<section class="sheet card-front" aria-label="Business card front">
  <div class="holder">
    <div class="holder-name">DANIEL HURST</div>
    <div class="holder-role">General Manager</div>
  </div>
  <div class="brand"><span class="brand-square"></span>KESTREL RELINING</div>
  <footer class="footer-band">
    <svg class="band-shape" viewBox="0 0 223 62" preserveAspectRatio="none" aria-hidden="true">
      <path class="band-dark" d="M0 0H78Q83 0 86 5L89 11Q91 15 96 15H223V62H0Z"/>
      <rect class="band-green" x="91" y="10" width="132" height="4.5"/>
    </svg>
    <div class="card-contact">
      <div class="info-line"><svg><use href="#icon-phone"/></svg>1-300-555-014</div>
      <div class="info-line"><svg><use href="#icon-mail"/></svg>hello@KestrelRelining.com.au</div>
      <div class="info-line"><svg><use href="#icon-globe"/></svg>www.KestrelRelining.com.au</div>
    </div>
    <div class="card-address">
      <div>14 Harbour Lane</div>
      <div>Dunmore NSW 2529</div>
      <div>ABN: 12 345 678 901</div>
    </div>
  </footer>
</section>

<!-- Business card back -->
<section class="sheet card-back" aria-label="Business card back">
  <div class="brand"><span class="brand-square"></span>KESTREL RELINING</div>
</section>

</body>
</html>
```